Ferrant Valley Zoning Council Business Cards

We're looking for a business card design, simple as that. We're a local government agency that mainly performs building code enforcement, transportation planning, floodplain management, and GIS for Tobelle Parish in Louisiana, and other surround parishes. So you're not having to Google anything, GIS is, at it's core, mapping. Building Code Enforcement is just that, nothing more. Floodplain Management is to make sure the public is within what the government

Contact Information for Business Card

Our Address is

517 Marwick Street
Alexandria, LA 71489

Our phone is 3185529137
Our fax is 3185529142
Our website is www.fvzc.info
My email is dana@fvzc.info

Font styles to use
Serif
Sans Serif

Colors

Designer to choose colors to be used in the design.

Requirements
Must have
• I'm attaching our logo(several versions) that must be incorporated. The design should fit well with our existing logo. I can send photoshop files for our logo if needed. If possible, I'd like to be able to add names/info to each card for all of our employees once this is done.
Nice to have
• The Louisiana state seal is a bonus, and isn't specifically required.

```html
<!DOCTYPE html>
<html lang="en">
<head>
<meta charset="utf-8">
<title>Ferrant Valley Zoning Council — Business Cards</title>
<link href="https://fonts.googleapis.com/css2?family=Montserrat:wght@400;500;600;700&display=swap" rel="stylesheet">
<style>
  :root {
    --page: #a9a9a9;
    --front-bg: #575757;
    --back-bg: #ffffff;
    --ink: #1a1a1a;
    --muted: #4a4a4a;
    --green: #22a52a;
    --seal: #1f3a78;
    --mark-green: #3bb54a;
    --mark-blue: #1c5fcf;
    --mark-lime: #c9df1f;
    --mark-orange: #ef9323;
  }
  * { box-sizing: border-box; margin: 0; padding: 0; }
  html, body { width: 1200px; height: 930px; overflow: hidden; }
  body {
    background: var(--page);
    font-family: "Montserrat", sans-serif;
    position: relative;
  }
  .card {
    position: absolute;
    width: 560px;
    height: 320px;
    border-radius: 18px;
    overflow: hidden;
    box-shadow: 0 6px 18px rgba(0,0,0,0.25);
  }
  .card--front { left: 80px; top: 90px; background: var(--front-bg); }
  .card--back { left: 560px; top: 510px; background: var(--back-bg); }

  .front-pattern {
    position: absolute;
    inset: 0;
    background:
      radial-gradient(ellipse at 35% 55%, rgba(80,110,160,0.35), transparent 55%),
      radial-gradient(ellipse at 70% 35%, rgba(110,130,80,0.30), transparent 50%),
      radial-gradient(ellipse at 20% 75%, rgba(150,110,60,0.25), transparent 45%);
  }

  .brand {
    position: absolute;
    display: flex;
    align-items: center;
    gap: 14px;
    font-weight: 600;
  }
  .brand__dot {
    width: 58px; height: 58px;
    border-radius: 50%;
    flex: none;
  }
  .brand__text { display: flex; flex-direction: column; line-height: 1; }
  .brand__short { font-size: 66px; letter-spacing: 1px; }
  .brand__long { font-size: 11px; letter-spacing: 0.5px; margin-top: 6px; }

  .card--front .brand { left: 120px; top: 112px; color: #ffffff; }
  .card--front .brand__dot { background: var(--mark-green); }

  .seal {
    position: absolute;
    right: 44px; top: 130px;
    width: 74px; height: 74px;
    border-radius: 50%;
    background: var(--seal);
    border: 4px solid #ffffff;
  }

  .card--back .brand { left: 38px; top: 124px; color: var(--ink); }
  .card--back .brand__dot { background: var(--mark-green); }
  .card--back .brand__short { font-size: 56px; }
  .card--back .brand__long { font-size: 10px; color: var(--ink); }

  .divider {
    position: absolute;
    left: 300px; top: 50px;
    width: 2px; height: 170px;
    background: var(--green);
  }
  .contact {
    position: absolute;
    left: 322px; top: 46px;
    color: var(--muted);
    font-size: 14px;
    line-height: 1.3;
  }
  .contact__name { color: var(--green); font-weight: 700; font-size: 20px; }
  .contact__role { margin-bottom: 10px; }
  .contact__address { margin-bottom: 10px; }
  .contact__list { list-style: none; }
  .contact__list li { display: flex; align-items: center; gap: 8px; }
  .contact__list svg { width: 11px; height: 11px; flex: none; fill: var(--green); }
</style>
</head>
<body>

<section class="card card--front" aria-label="Card front">
  <div class="front-pattern" role="img" aria-label="Soft blocks of muted blue, green and amber tones behind the name"></div>
  <div class="brand">
    <span class="brand__dot"></span>
    <span class="brand__text">
      <span class="brand__short">FVZC</span>
      <span class="brand__long">Ferrant Valley Zoning Council</span>
    </span>
  </div>
  <div class="seal" role="img" aria-label="State seal badge"></div>
</section>

<section class="card card--back" aria-label="Card back">
  <div class="brand">
    <span class="brand__dot"></span>
    <span class="brand__text">
      <span class="brand__short">FVZC</span>
      <span class="brand__long">Ferrant Valley Zoning Council</span>
    </span>
  </div>
  <div class="divider"></div>
  <div class="contact">
    <p class="contact__name">Dana Whitcombe</p>
    <p class="contact__role">Director</p>
    <p class="contact__address">517 Marwick Street<br>Alexandria, LA 71489</p>
    <ul class="contact__list">
      <li><svg viewBox="0 0 12 12"><path d="M2.5 1 4.5 3.2 3.6 4.6c.7 1.5 2 2.8 3.6 3.6l1.3-.9L11 9.5 9.8 11C5.2 10.7 1.3 6.8 1 2.2Z"/></svg>3185529137</li>
      <li><svg viewBox="0 0 12 12"><path d="M3 1h5v3H3ZM1 5h10v4H9v2H3V9H1Zm3 3v2h4V8Z"/></svg>3185529142</li>
      <li><svg viewBox="0 0 12 12"><path d="M1 2.5h10v7H1Zm1 1v.4l4 2.6 4-2.6v-.4Zm0 1.6v3.4h8V5.1L6 7.7Z"/></svg>dana@fvzc.info</li>
      <li><svg viewBox="0 0 12 12"><path d="M6 1a5 5 0 1 0 0 10A5 5 0 0 0 6 1Zm0 1c.6.6 1 1.7 1.1 3H4.9C5 3.7 5.4 2.6 6 2ZM2.1 5h1.8c0-1 .3-1.9.6-2.6A4 4 0 0 0 2.1 5Zm5.4-2.6c.3.7.6 1.6.6 2.6h1.8a4 4 0 0 0-2.4-2.6ZM2.1 7a4 4 0 0 0 2.4 2.6c-.3-.7-.6-1.6-.6-2.6Zm2.8 0c.1 1.3.5 2.4 1.1 3 .6-.6 1-1.7 1.1-3Zm3.2 0c0 1-.3 1.9-.6 2.6A4 4 0 0 0 9.9 7Z"/></svg>www.fvzc.info</li>
    </ul>
  </div>
</section>

</body>
</html>
```